New Web Design Project

We are working with Brelvin Aggregates (https://brelvinaggregates.example) and are seeking a website design that reflects a modern, professional, and industry-appropriate aesthetic. Here’s some details on what we’re looking for on the website redesign.
Home page:
Our video playing - with numbers rolling for totals:
drivers, tons hauled, miles of roads paved, dirt moved, rock hauled
Competitor & Inspiration Sites:
(We will include links to competitor or inspirational websites to help guide your creative direction.)
tolmquay.example - Transitions
plinwerk.example - Color contrasts & dynamic logo
duvrana.example - Dynamic tabs
⸻
About Us & How We Work
Thank you for taking the time to consider designing a website for us. We are a web development agency based in Stockton, California (USA). Most of our projects follow a consistent process, and understanding how we work may help increase your chances of being selected.
All websites are custom-coded in-house. While there are no restrictions on the tools you use to design, Figma files are preferred.
⸻
Our Design Selection Process
Designs that meet our quality standards may be marked as four-star designs. These designs are presented to the client, who selects the final concept we move forward with.
Once a design reaches this stage, it may also be reused as inspiration or presented to future clients. This means your design can have multiple opportunities to sell, even beyond the original project.
To improve your chances of success, please follow the guidelines below.
⸻
Image & Icon Usage
If you include images or icons in your design, please provide a link to the source so we can purchase the asset.
• Stock imagery is encouraged.
• Focus on conveying the mood, tone, and personality of the brand.
• You may use any royalty-free image provider., but we primarily use Vemora Images, but we are open to purchasing assets from other platforms.
⸻
Fonts
Please identify the fonts used in your design (a message is sufficient).
• We only use Google Fonts and Adobe Fonts.
• Clean, legible typography is strongly preferred.
⸻
Content Guidelines
We welcome creative ideas and layout suggestions.
• Stock images are commonly used to communicate the design vision.
• Client-specific photography is often added after launch.
• Lorem Ipsum is acceptable for paragraph text.
• Please write real, properly written English headings so we can clearly understand section intent and structure.
⸻
Inspiration
We typically include a few reference websites in the brief to help establish visual direction. These are meant as inspiration—not templates.
⸻
Revisions
We rarely request design revisions.
• If we see a concept that may not resonate with the client, we may ask for clarification or adjustment.
• Minor refinements are typically handled during the development phase rather than the design phase.
⸻
Feedback
Due to the volume of projects we manage, we generally do not provide ongoing feedback during the design process.
• Well-thought-out questions that are specific and actionable may receive a response.
• General requests such as “feedback, please” typically go unanswered.
⸻
Client Communication
All communication regarding this project must remain within PitchHarbor and with our team only.
• Designers may not contact the client directly under any circumstances.
• If a designer reaches out to the client outside of PitchHarbor and we become aware of it, the incident will be reported to PitchHarbor.
• To protect both the client and the integrity of the design process, we often use placeholder or internal brand names when launching design projects.
This policy is non-negotiable and helps ensure a fair, professional, and organized process for everyone involved.

```html
<!DOCTYPE html>
<html lang="en">
<head>
<meta charset="utf-8">
<title>Brelvin Aggregates – Home</title>
<link rel="stylesheet" href="https://fonts.googleapis.com/css2?family=Inter:wght@400;500;600;700&display=swap">
<style>
  :root {
    --ink: #1a1a1a;
    --muted: #3a3a3a;
    --page: #ffffff;
    --accent: #e2722c;
    --note: #7a0019;
    --footer: #1a1718;
  }
  * { margin: 0; padding: 0; box-sizing: border-box; }
  html, body { width: 1200px; height: 645px; overflow: hidden; background: var(--page); }
  body { position: relative; font-family: "Inter", Arial, sans-serif; color: var(--ink); }

  .stat { position: absolute; top: 4px; width: 240px; margin-left: -120px; text-align: center; }
  .stat-value { font-size: 27px; font-weight: 700; letter-spacing: 0.2px; line-height: 34px; }
  .stat-label { margin-top: 13px; font-size: 9.5px; letter-spacing: 1.6px; color: var(--muted); text-transform: uppercase; }

  .note { position: absolute; color: var(--note); font-weight: 700; white-space: nowrap; transform: translateX(-50%); }
  .note-title { top: 74px; left: 525px; font-size: 11.5px; }
  .note-cards { top: 353px; left: 583px; font-size: 12.5px; letter-spacing: 0.2px; }
  .note-culture { top: 412px; left: 514px; font-size: 12.5px; letter-spacing: 0.2px; }

  .annotation-lines { position: absolute; left: 0; top: 0; width: 1200px; height: 645px; pointer-events: none; }
  .annotation-lines line { stroke: var(--note); stroke-width: 2.4; stroke-linecap: round; }

  .section-title { position: absolute; left: 50px; font-size: 15px; font-weight: 700; }
  .what-title { top: 158px; }
  .what-lead { position: absolute; left: 50px; top: 181px; font-size: 10px; color: var(--muted); }
  .how-title { top: 386px; }

  .service-card {
    position: absolute; top: 223px; width: 263px; height: 56px;
    background: #fff; border: 1px solid #ececec;
    box-shadow: 2px 3px 6px rgba(0,0,0,0.18);
    padding-left: 19px; display: flex; align-items: center;
    font-size: 10px; font-weight: 600;
  }

  .step { position: absolute; top: 490px; width: 231px; }
  .step-name { font-size: 10px; padding-left: 12px; color: var(--ink); }
  .step-rule { margin-top: 14px; height: 2px; background: var(--accent); }

  .site-footer { position: absolute; left: 0; top: 612px; width: 1200px; height: 33px; background: var(--footer); }
  .footer-tab { position: absolute; left: 564px; top: 0; width: 62px; height: 7px; background: var(--accent); }
</style>
</head>
<body>
  <section class="stats">
    <div class="stat" style="left:156px"><div class="stat-value">2500</div><div class="stat-label">Drivers</div></div>
    <div class="stat" style="left:449px"><div class="stat-value">18,000,000</div><div class="stat-label">Tons Hauled</div></div>
    <div class="stat" style="left:742px"><div class="stat-value">4200</div><div class="stat-label">Miles Paved</div></div>
    <div class="stat" style="left:1034px"><div class="stat-value">50</div><div class="stat-label">Years Experience</div></div>
  </section>

  <p class="note note-title">Annotated layout explaining section structure and responsiveness - Part 2</p>

  <section class="what-we-do">
    <h2 class="section-title what-title">What We Do</h2>
    <p class="what-lead">End-to-end materials and logistics solutions for California’s largest projects.</p>
    <div class="service-card" style="left:50px">Aggregates &amp; Materials</div>
    <div class="service-card" style="left:326px">Transportation &amp; Logistics</div>
    <div class="service-card" style="left:602px">Infrastructure Support</div>
    <div class="service-card" style="left:877px">Project Partnerships</div>
  </section>

  <svg class="annotation-lines" viewBox="0 36 1920 996" preserveAspectRatio="none" aria-hidden="true">
    <line x1="292" y1="494" x2="741" y2="600" vector-effect="non-scaling-stroke"/>
    <line x1="680" y1="477" x2="758" y2="572" vector-effect="non-scaling-stroke"/>
    <line x1="1036" y1="486" x2="992" y2="571" vector-effect="non-scaling-stroke"/>
    <line x1="1444" y1="483" x2="1129" y2="578" vector-effect="non-scaling-stroke"/>
    <line x1="745" y1="693" x2="226" y2="788" vector-effect="non-scaling-stroke"/>
    <line x1="813" y1="701" x2="678" y2="777" vector-effect="non-scaling-stroke"/>
    <line x1="855" y1="704" x2="995" y2="779" vector-effect="non-scaling-stroke"/>
    <line x1="900" y1="698" x2="1419" y2="792" vector-effect="non-scaling-stroke"/>
  </svg>

  <p class="note note-cards">Headlines Cards for Domain of work</p>

  <section class="how-we-work">
    <h2 class="section-title how-title">How We Work</h2>
    <div class="step" style="left:70px"><div class="step-name">Source</div><div class="step-rule"></div></div>
    <div class="step" style="left:343px"><div class="step-name">Coordinate</div><div class="step-rule"></div></div>
    <div class="step" style="left:616px"><div class="step-name">Deliver</div><div class="step-rule"></div></div>
    <div class="step" style="left:889px"><div class="step-name">Build</div><div class="step-rule"></div></div>
  </section>

  <p class="note note-culture">Work Culture</p>

  <footer class="site-footer"><span class="footer-tab"></span></footer>
</body>
</html>
```